label update for bottle change

The goal is to adapt the label's design and shape to the new bottle, maintaining its defining elements such as the font, vertical name, company logo, background pattern, and color. The new design should not be identical to the old one, but rather an evolution of it. The gold stripe on the bottom is not mandatory, but the writing "BASSANO DEL GRAPPA / EST. 1886" must be retained, slightly enlarged.

The font name is: Brandon Text

```html
<!DOCTYPE html>
<html lang="it">
<head>
<meta charset="utf-8">
<title>Carciofo – Amaro di Carattere label</title>
<link rel="stylesheet" href="https://fonts.googleapis.com/css2?family=Montserrat:wght@500;600;700;800&display=swap">
<style>
  :root {
    --backdrop: #f2f5dc;
    --label-purple: #4e1d63;
    --ink-white: #f7f5f2;
    --ink-grey: #4a4746;
    --gold-dark: #8a5a1a;
    --gold-mid: #d4a34a;
    --gold-light: #e0b865;
    --wine: #6a2a26;
    --art-red: #c8283a;
    --art-olive: #5d5a3a;
    --art-green: #1f5a45;
  }
  html, body {
    margin: 0;
    padding: 0;
    width: 1200px;
    height: 1200px;
    overflow: hidden;
    background: var(--backdrop);
    font-family: "Montserrat", sans-serif;
  }
  .label {
    position: absolute;
    left: 270px;
    top: 160px;
    width: 660px;
    height: 880px;
    background: var(--label-purple);
    overflow: hidden;
  }
  .maker {
    position: absolute;
    right: 40px;
    top: 66px;
    text-align: right;
    color: var(--ink-white);
  }
  .maker-line {
    display: block;
    font-size: 19px;
    font-weight: 500;
    letter-spacing: 0.3em;
    margin-right: -0.3em;
    line-height: 1;
  }
  .maker-name {
    display: block;
    margin-top: 8px;
    font-size: 36px;
    font-weight: 800;
    line-height: 1;
    letter-spacing: 0;
  }
  .product-name {
    position: absolute;
    left: 166px;
    bottom: 122px;
    margin: 0;
    writing-mode: vertical-rl;
    transform: rotate(180deg);
    color: var(--ink-white);
    font-size: 100px;
    font-weight: 700;
    line-height: 1;
    letter-spacing: 0.02em;
    white-space: nowrap;
  }
  .product-type {
    position: absolute;
    left: 112px;
    bottom: 124px;
    writing-mode: vertical-rl;
    transform: rotate(180deg);
    color: var(--ink-grey);
    font-size: 33px;
    font-weight: 500;
    line-height: 1;
    letter-spacing: 0.1em;
    white-space: nowrap;
  }
  .artichoke {
    position: absolute;
    left: 297px;
    top: 300px;
    width: 323px;
    height: 500px;
    border-radius: 48% 48% 20% 20% / 40% 40% 12% 12%;
    background: linear-gradient(180deg, var(--art-red) 0%, var(--art-red) 18%, var(--art-olive) 36%, var(--art-green) 62%, var(--art-green) 100%);
  }
  .origin-band {
    position: absolute;
    left: 0;
    bottom: 0;
    width: 100%;
    height: 80px;
    background: linear-gradient(90deg, var(--gold-dark) 0%, var(--gold-mid) 25%, var(--gold-light) 50%, var(--gold-mid) 72%, var(--wine) 100%);
  }
  .origin-text {
    position: absolute;
    right: 90px;
    top: 50%;
    transform: translateY(-50%);
    margin: 0;
    color: var(--ink-white);
    font-size: 22px;
    font-weight: 700;
    letter-spacing: 0.05em;
    white-space: nowrap;
  }
</style>
</head>
<body>
  <main class="label">
    <div class="maker">
      <span class="maker-line">FABBRICA LIQUORI</span>
      <span class="maker-name">F.LLI MARCOLINI</span>
    </div>

    <div class="product-type">AMARO DI CARATTERE</div>
    <h1 class="product-name">CARCIOFO</h1>

    <div class="artichoke" role="img" aria-label="Engraved-style illustration of an artichoke head on its stem, red tips fading to green leaves"></div>

    <div class="origin-band">
      <p class="origin-text">BASSANO DEL GRAPPA / EST. 1886</p>
    </div>
  </main>
</body>
</html>
```